Criação de Layout de Rótulo para Limpeza & Serviço para o lar
A empresa queria:
" ESTAMOS HÁ 42 ANOS FABRICANDO E VENDENDO OS MELHORES PRODUTOS DE LIMPEZA "

```html
<!DOCTYPE html>
<html lang="pt-BR">
<head>
<meta charset="UTF-8">
<title>Doces Suspiros – Home Spray – Rótulos</title>
<link href="https://fonts.googleapis.com/css2?family=Montserrat:wght@400;600;800&family=Playfair+Display:wght@700&display=swap" rel="stylesheet">
<style>
  :root {
    --canvas: #ffffff;
    --label-bg: #fbfafc;
    --ink: #6e6a70;
    --pink-band-top: #f7d3df;
    --pink-band-bottom: #eeb2c6;
    --pink-brand: #d9437b;
    --pink-title: #7b4f5d;
    --pink-pattern: #f6e6ec;
    --lilac-band-top: #e4daf0;
    --lilac-band-bottom: #cfbfe6;
    --lilac-brand: #8c68b8;
    --lilac-title: #5f4d73;
    --lilac-pattern: #eee8f5;
    --blue-band-top: #dbe6f5;
    --blue-band-bottom: #bccfeb;
    --blue-brand: #3d72b8;
    --blue-title: #4a5a72;
    --blue-pattern: #e6edf7;
  }
  * { box-sizing: border-box; margin: 0; padding: 0; }
  html, body {
    width: 1200px;
    height: 1200px;
    overflow: hidden;
    background: var(--canvas);
  }
  .label-set {
    position: absolute;
    inset: 0;
    display: flex;
    justify-content: center;
    align-items: center;
    gap: 36px;
  }
  .label {
    position: relative;
    width: 356px;
    height: 760px;
    background: var(--label-bg);
    overflow: hidden;
    box-shadow: 0 0 0 1px #ecebee;
  }
  .label--pink  { --band-top: var(--pink-band-top);  --band-bottom: var(--pink-band-bottom);  --brand: var(--pink-brand);  --title: var(--pink-title);  --pattern: var(--pink-pattern); }
  .label--lilac { --band-top: var(--lilac-band-top); --band-bottom: var(--lilac-band-bottom); --brand: var(--lilac-brand); --title: var(--lilac-title); --pattern: var(--lilac-pattern); }
  .label--blue  { --band-top: var(--blue-band-top);  --band-bottom: var(--blue-band-bottom);  --brand: var(--blue-brand);  --title: var(--blue-title);  --pattern: var(--blue-pattern); }

  .floral-pattern {
    position: absolute;
    inset: 0;
    background: linear-gradient(160deg, var(--label-bg) 0%, var(--pattern) 50%, var(--label-bg) 100%);
  }
  .color-band {
    position: absolute;
    top: 0;
    bottom: 0;
    left: 68px;
    width: 220px;
    background: linear-gradient(180deg, var(--band-top), var(--band-bottom) 55%, var(--band-top));
  }
  .label-content {
    position: absolute;
    inset: 0;
    display: flex;
    flex-direction: column;
    align-items: center;
    text-align: center;
    padding-top: 122px;
  }
  .brand-name {
    font-family: 'Montserrat', sans-serif;
    font-weight: 800;
    font-size: 34px;
    color: var(--brand);
    line-height: 1;
  }
  .product-type {
    margin-top: 116px;
    font-family: 'Montserrat', sans-serif;
    font-weight: 400;
    font-size: 17px;
    line-height: 1.25;
    color: var(--ink);
  }
  .product-name {
    margin-top: 66px;
    font-family: 'Montserrat', sans-serif;
    font-weight: 600;
    font-size: 22px;
    line-height: 1;
    color: var(--title);
  }
  .product-line {
    margin-top: 14px;
    font-family: 'Montserrat', sans-serif;
    font-weight: 400;
    font-size: 14px;
    letter-spacing: 4px;
    color: var(--ink);
  }
  .fragrance {
    margin-top: 56px;
    font-family: 'Playfair Display', serif;
    font-weight: 700;
    font-size: 20px;
    color: var(--title);
  }
  .volume {
    margin-top: 60px;
    font-family: 'Montserrat', sans-serif;
    font-weight: 400;
    font-size: 17px;
    color: var(--ink);
  }
</style>
</head>
<body>
  <main class="label-set">
    <section class="label label--pink">
      <div class="floral-pattern" role="img" aria-label="Padrão floral em linhas rosa-claro ao fundo do rótulo"></div>
      <div class="color-band"></div>
      <div class="label-content">
        <p class="brand-name">Brisa Lar</p>
        <p class="product-type">Aromatizador<br>de ambiente</p>
        <h2 class="product-name">Doces Suspiros</h2>
        <p class="product-line">HOME SPRAY</p>
        <p class="fragrance">lavanda</p>
        <p class="volume">250ml</p>
      </div>
    </section>

    <section class="label label--lilac">
      <div class="floral-pattern" role="img" aria-label="Padrão floral em linhas lilás-claro ao fundo do rótulo"></div>
      <div class="color-band"></div>
      <div class="label-content">
        <p class="brand-name">Brisa Lar</p>
        <p class="product-type">Aromatizador<br>de ambiente</p>
        <h2 class="product-name">Doces Suspiros</h2>
        <p class="product-line">HOME SPRAY</p>
        <p class="fragrance">lavanda</p>
        <p class="volume">250ml</p>
      </div>
    </section>

    <section class="label label--blue">
      <div class="floral-pattern" role="img" aria-label="Padrão floral em linhas azul-claro ao fundo do rótulo"></div>
      <div class="color-band"></div>
      <div class="label-content">
        <p class="brand-name">Brisa Lar</p>
        <p class="product-type">Aromatizador<br>de ambiente</p>
        <h2 class="product-name">Doces Suspiros</h2>
        <p class="product-line">HOME SPRAY</p>
        <p class="fragrance">lavanda</p>
        <p class="volume">250ml</p>
      </div>
    </section>
  </main>
</body>
</html>
```